Cardiology Practice needs Imaging Order Form

Busy Cardiology Practice needs an imaging order form for its various types of imaging services. A sample has been uploaded. Our primary colors are red, black and white. Design should be able to fit 8 1/2 by 11 paper. Would like order form on one side and minimally the map on the other side with our demographic information which is Coral Ridge Cardiac, PLLC located at 718 Tamber Ln. Ste. K, Webster, TX 77412. Phone is 713-264-8817, Fax is 713-264-8817, and our web address is coralridgecardiac.example. Our physicians names are Dorin Melvik, MD, G.L. Vombrasca, MD, Ottilie Granby, MD, Corwin Melvik, MD, and Leopold Danforth, MD. We also have 3 nurse practitioners whose names are Ruthie Marbeck, MSN, ACNP-BC, Delia Fairclough, MSN, APRN, AGNP-C and Minette Oakes, MSN, APRN, NP-C.

Target Market(s)

Healthcare

Industry/Entity Type

Healthcare

Font styles to use
Serif

Colors
ec1f27

Requirements
Must have
• All testing on sample order form uploaded. Clinic Logo, Map, Demographic Information, physician and nurse practitioner information and website.
Nice to have
• Open to suggestions
Should not have
• physician or nurse practitioner pictures

```html
<!DOCTYPE html>
<html lang="en">
<head>
<meta charset="utf-8">
<title>Imaging Service Order Form</title>
<link href="https://fonts.googleapis.com/css2?family=Oswald:wght@700&family=Lato:wght@400;700&display=swap" rel="stylesheet">
<style>
:root{
  --red:#d1343c;
  --red-bright:#ec1f27;
  --black:#111111;
  --ink:#1d1d1d;
  --line:#555555;
  --paper:#ffffff;
  --backdrop:#e9e6e3;
}
*{box-sizing:border-box;margin:0;padding:0}
html,body{width:1200px;height:1200px;overflow:hidden;background:var(--backdrop);font-family:"Lato",sans-serif;color:var(--ink)}
.sheet{position:absolute;left:154px;top:18px;width:892px;height:1164px;background:var(--paper);box-shadow:0 6px 24px rgba(0,0,0,.18);overflow:hidden}
.header{position:absolute;left:0;top:0;width:100%;height:142px}
.brand{position:absolute;left:34px;top:62px;display:flex;align-items:center;gap:8px}
.brand-dot{width:18px;height:18px;border-radius:50%;background:var(--red)}
.brand-name{font-family:"Lato",sans-serif;font-weight:700;font-size:15px;color:var(--red);line-height:1.1;width:110px}
.title{position:absolute;left:196px;top:44px;font-family:"Oswald",sans-serif;font-weight:700;font-size:52px;letter-spacing:.5px;color:var(--black)}
.contact{position:absolute;left:612px;top:16px;font-size:12px;line-height:1.35}
.contact div{display:flex;align-items:center;gap:6px}
.contact svg{width:11px;height:11px;flex:none}
.contact .phone{font-weight:700}
.requisition{position:absolute;left:602px;top:80px;width:258px;border:1px solid var(--black);font-size:13px}
.requisition div{height:22px;border-bottom:1px solid var(--black);padding:3px 8px}
.requisition div:last-child{border-bottom:0}
.requisition .req-title{text-align:center}
.rule{position:absolute;left:0;width:100%;height:2px;background:var(--red)}
.staff{position:absolute;left:34px;top:150px;width:560px;font-size:14px;line-height:1.3}
.staff .nurses{display:flex;gap:8px;margin-top:2px}
.staff .nurses b{color:var(--red);white-space:nowrap}
.panel{position:absolute;border:1px solid var(--black)}
.panel h2{background:var(--black);color:#fff;font-family:"Lato",sans-serif;font-weight:400;font-size:21px;letter-spacing:.5px;padding:6px 20px 4px;text-transform:uppercase}
.field{position:absolute;font-size:11px}
.uline{position:absolute;height:1.5px;background:var(--black)}
.box{display:inline-block;width:18px;height:18px;border:1px solid var(--black);vertical-align:middle}
.choice{display:inline-block;border:1px solid var(--black);padding:2px 12px;font-size:11px}
.read-first{position:absolute;left:42px;top:640px;font-size:13.5px}
.read-first b{font-weight:700}
.col{position:absolute;top:676px}
.pill{display:inline-block;background:var(--red);color:#fff;font-size:16px;font-weight:700;padding:3px 12px;border-radius:14px;margin-bottom:6px}
.sub{font-size:16px;font-weight:700;margin:2px 0 4px}
.item{display:flex;justify-content:space-between;align-items:center;font-size:13px;line-height:1.2;min-height:22px}
.item .box{width:28px;height:16px;border-radius:1px;flex:none;margin-left:8px}
.group{margin-bottom:14px}
.unlisted{margin-top:30px;border-top:1.5px solid var(--black);padding-top:6px;font-size:13px;font-weight:700;line-height:1.3}
.footer-band{position:absolute;left:0;bottom:0;width:100%;height:30px;background:var(--red)}
</style>
</head>
<body>
<main class="sheet">
  <header class="header">
    <div class="brand"><span class="brand-dot"></span><span class="brand-name">Coral Ridge Cardiac, PLLC</span></div>
    <h1 class="title">IMAGING SERVICE</h1>
    <div class="contact">
      <div class="phone"><svg viewBox="0 0 12 12"><circle cx="6" cy="6" r="5.3" fill="none" stroke="#d1343c" stroke-width="1.2"/><path d="M4 3.5l1 1-.6.9a4 4 0 0 0 2.2 2.2l.9-.6 1 1-.8.9C5.8 8.8 3.2 6.2 3.1 4.3z" fill="#d1343c"/></svg>713-264-8817</div>
      <div><svg viewBox="0 0 12 12"><circle cx="6" cy="6" r="5.2" fill="none" stroke="#d1343c" stroke-width="1.1"/><path d="M.8 6h10.4M6 .8c-2.4 2.8-2.4 7.6 0 10.4M6 .8c2.4 2.8 2.4 7.6 0 10.4" fill="none" stroke="#d1343c" stroke-width=".9"/></svg>www.coralridgecardiac.example</div>
      <div><svg viewBox="0 0 12 12"><path d="M6 11.5S2 7.2 2 4.6a4 4 0 0 1 8 0C10 7.2 6 11.5 6 11.5z" fill="#d1343c"/><circle cx="6" cy="4.6" r="1.4" fill="#fff"/></svg>718 Tamber Ln. Ste. K, Webster, TX 77412</div>
    </div>
    <div class="requisition">
      <div class="req-title">Service Requisition</div>
      <div>Date :</div>
      <div>Time :</div>
      <div>Solicitor :</div>
    </div>
  </header>

  <div class="rule" style="top:142px"></div>

  <section class="staff">
    <p>Dorin Melvik, MD, G.L. Vombrasca, MD, Ottilie Granby, MD, Corwin Melvik, MD, and Leopold Danforth, MD.</p>
    <p class="nurses"><b>Our Nurses :</b><span>Ruthie Marbeck, MSN, ACNP-BC, Delia Fairclough, MSN, APRN, AGNP-C and Minette Oakes, MSN, APRN, NP-C.</span></p>
  </section>

  <div class="rule" style="top:242px"></div>

  <section class="panel" style="left:34px;top:262px;width:408px;height:150px">
    <h2>Patient Information</h2>
    <span class="field" style="left:14px;top:68px">Last name</span>
    <span class="field" style="left:150px;top:52px">First name</span>
    <span class="field" style="left:320px;top:52px">MI</span>
    <div class="uline" style="left:14px;top:66px;width:330px"></div>
    <span class="field" style="left:230px;top:78px">Sex <span class="box"></span> M <span class="box" style="margin-left:14px"></span> F</span>
    <span class="field" style="left:14px;top:104px">Date of Birth</span>
    <div class="uline" style="left:14px;top:130px;width:180px"></div>
  </section>

  <section class="panel" style="left:472px;top:262px;width:388px;height:150px">
    <h2>Contact Information</h2>
    <div class="uline" style="left:14px;top:62px;width:360px"></div>
    <span class="field" style="left:14px;top:70px">Address</span>
    <span class="field" style="left:210px;top:70px">Mobile Ph no</span>
    <div class="uline" style="left:210px;top:104px;width:160px"></div>
    <span class="field" style="left:14px;top:104px">Home Ph no</span>
    <div class="uline" style="left:14px;top:134px;width:170px"></div>
  </section>

  <section class="panel" style="left:34px;top:430px;width:408px;height:186px">
    <h2>Medical Information</h2>
    <span class="field" style="left:70px;top:48px">ICD-10</span>
    <span class="field" style="left:210px;top:42px">Narrative diagnosis</span>
    <div class="uline" style="left:0;top:64px;width:406px;height:1px;background:var(--line)"></div>
    <span class="field" style="left:30px;top:88px">1.</span>
    <div class="uline" style="left:0;top:104px;width:406px;height:1px;background:var(--line)"></div>
    <span class="field" style="left:30px;top:110px">2.</span>
    <span class="field" style="left:280px;top:108px">Signature</span>
    <div class="uline" style="left:250px;top:130px;width:150px;height:2px"></div>
    <span class="field" style="left:30px;top:132px">3.</span>
    <span class="field" style="left:30px;top:150px">Prescriber's name</span>
    <div class="uline" style="left:30px;top:172px;width:170px;height:2px"></div>
  </section>

  <section class="panel" style="left:472px;top:430px;width:388px;height:186px">
    <h2>Insurance Information</h2>
    <span class="field" style="left:14px;top:52px">Primary insurance</span>
    <span class="field" style="left:210px;top:46px">Suscribers no.</span>
    <div class="uline" style="left:14px;top:80px;width:360px"></div>
    <span class="field" style="left:14px;top:92px">Authorization required?</span>
    <span class="field" style="left:210px;top:88px">Authorization no.</span>
    <div class="uline" style="left:210px;top:112px;width:160px"></div>
    <span class="field" style="left:14px;top:114px"><span class="choice">Yes</span> <span class="choice" style="margin-left:10px">No</span></span>
    <span class="field" style="left:210px;top:120px">STAT</span>
    <span class="field" style="left:210px;top:136px"><span class="choice">Yes</span> <span class="choice" style="margin-left:10px">No</span></span>
    <span class="field" style="left:14px;top:146px">Fax no.</span>
    <div class="uline" style="left:14px;top:170px;width:160px"></div>
  </section>

  <p class="read-first"><b>READ FIRST:</b> Please check any that apply and attach referral if available. The patient will be contacted for further instructions.</p>

  <section class="col" style="left:42px;width:262px">
    <div class="group">
      <span class="pill">Electrophysiology</span>
      <div class="item">Electrocardiograms (EKG)<span class="box"></span></div>
      <div class="item">Holter monitor (specify number of days: 3-14)<span class="box"></span></div>
      <div class="item">Implantable loop recorder placement<span class="box"></span></div>
      <div class="item">Implantable loop recorder monitoring<span class="box"></span></div>
      <div class="item">Pacemaker check<span class="box"></span></div>
      <div class="item">Pacemaker monitoring<span class="box"></span></div>
      <div class="item">Internal cardiac defibrillator (ICD) check<span class="box"></span></div>
      <div class="item">Internal cardiac defibrillator (ICD) monitoring<span class="box"></span></div>
    </div>
    <div class="group">
      <span class="pill">Cardiac imaging</span>
      <div class="item">Echocardiogram<span class="box"></span></div>
      <div class="item">Echocardiogram with bubble study<span class="box"></span></div>
      <div class="item">Calcium score (Heart scan)<span class="box"></span></div>
      <div class="item">Cardiac PET-CT<span class="box"></span></div>
    </div>
  </section>

  <section class="col" style="left:330px;width:270px">
    <div class="group">
      <span class="pill">Vascular imaging</span>
      <div class="item">Carotid doppler<span class="box"></span></div>
      <div class="item">Arterial doppler<span class="box"></span></div>
      <div class="item">Upper extremities<span class="box"></span></div>
      <div class="item">Lower extremities<span class="box"></span></div>
      <div class="item">Abdominal aorta<span class="box"></span></div>
      <div class="item">Renal arteries<span class="box"></span></div>
      <div class="item">Venous doppler of the lower extremities (LE)<span class="box"></span></div>
      <div class="item">Venous doppler of the LE with reflux study<span class="box"></span></div>
    </div>
    <div class="group">
      <span class="pill">Other specialized testing and therapies</span>
      <div class="item">Autonomic nervous system (ANS) testing<span class="box"></span></div>
      <div class="item">Enhanced external counter pulsation (EECP)<span class="box"></span></div>
      <div class="item">PulseTrack heart failure monitoring<span class="box"></span></div>
      <div class="item">Home sleep study<span class="box"></span></div>
    </div>
  </section>

  <section class="col" style="left:626px;width:232px">
    <div class="group">
      <span class="pill">Anticoagulation</span>
      <div class="item">INR &amp; PT<span class="box"></span></div>
    </div>
    <div class="group">
      <div class="sub">Cardiac stress test</div>
      <div class="item">Treadmill stress test<span class="box"></span></div>
      <div class="item">Tracerite stress test<span class="box"></span></div>
      <div class="item">VASOSCAN stress test<span class="box"></span></div>
      <div class="item">Stress test with echocardiogram<span class="box"></span></div>
      <div class="item">Dobutamine stress test with echocardiogram<span class="box"></span></div>
    </div>
    <div class="unlisted">Other unlisted procedures<br>or special instructions:</div>
  </section>

  <div class="footer-band"></div>
</main>
</body>
</html>
```